Start-up lawncare company needing marketing flyer to promote business model

Hello! We are looking for a marketing flyer design with the requirements below.

We would like the size to fit a flyer that is 6.25" X 9", Front and Back.

We need these to meet the KBMR ORTQ requirements, there are details attached for the indicias that need to be included, and where to put them on the back of the flyer.

Here's the items items we would like to have included on the flyer:
- Logo (Attached)

- I attached a snip of how our website looks, as well as how our app looks, and would like to follow that general color scheme

- References to our Fernquill App, in both Zenthra and Vorby stores, and our website (www.Fernquill.com)

- Reference to the neighborhood barometer and gets the point across that the more of their neighbors that sign up, the cheaper the price of service (Visual attached of what this barometer looks like)

- We are licensed and insured landscaping pros

- Real, instant, upfront pricing for mowing, mulching and most other services

- Sign up with a few easy steps and manage your account from our app or online

- Automated safe & secure transactions upon service completion and satisfaction

- Excellent customer service with our quality guaranteed commitment!

- Sign up now and receive 50% off your first mow!

- Veteran owned

- A portion of our proceeds go to "Rennick Dolby Foundation"

- List's out all of the services we will offer
- Mowing
- Mulching
- Aeration and Over-seeding
- Fertilization
- Shrub/Tree Trimming
- Leaf removal and yard clean up
- Accent lighting installation
- Sprinkler blow-out / Winterization
- Driveway pressure washing and sealing
- Firewood Delivery

Target Market(s)

Homeowners in large neighborhoods that need lawn care services

Industry/Entity Type

Lawn Care

Font styles to use
Sans Serif

Colors

Designer to choose colors to be used in the design.

Requirements
Must have
• Meet KBMR ORTQ requirements
• Keep a similar color scheme to our website, feel free to use bold accents to make it more eye-catching as people search through their mail
• Get the general point across that as more of their neighbors sign up with us, the cheaper their service will be

```html
<!DOCTYPE html>
<html lang="en">
<head>
<meta charset="utf-8">
<title>Fernquill Postcard – Front and Back</title>
<link rel="stylesheet" href="https://fonts.googleapis.com/css2?family=Oswald:wght@500;600;700&family=Roboto+Condensed:wght@400;700&family=Montserrat:wght@600;700;800;900&family=Arimo&display=swap">
<style>
  :root {
    --green: #3bb143;
    --green-dark: #2a9a3a;
    --teal: #1fa88c;
    --navy: #243f95;
    --sky: #2aa7e1;
    --white: #ffffff;
    --page: #ececec;
    --grey-track: #dcdcdc;
    --ink: #222;
  }
  * { box-sizing: border-box; margin: 0; padding: 0; }
  html, body { width: 979px; height: 1200px; overflow: hidden; background: var(--page); }
  .sheet { position: relative; width: 979px; height: 1200px; }
  .card {
    position: absolute; left: 89.5px; width: 891px; height: 618px;
    background: var(--white); overflow: hidden;
    transform: scale(0.898); transform-origin: top left;
    font-family: "Roboto Condensed", Arial, sans-serif;
    box-shadow: 0 6px 14px rgba(0,0,0,.25);
  }
  .card--front { top: 30px; }
  .card--back { top: 615px; }
  .abs { position: absolute; }

  /* Front */
  .brand { left: 20px; top: 62px; width: 150px; display: flex; align-items: center; gap: 6px; }
  .brand__dot { width: 14px; height: 14px; background: var(--green); border-radius: 50%; flex: none; }
  .brand__name { font-family: "Oswald", sans-serif; font-weight: 700; font-size: 30px; color: var(--navy); letter-spacing: .5px; }
  .headline { left: 196px; top: 20px; font-family: "Oswald", sans-serif; font-weight: 700; line-height: 1.05; }
  .headline__top { color: var(--green); font-size: 33px; letter-spacing: .5px; }
  .headline__sub { color: var(--navy); font-size: 27px; letter-spacing: .5px; }
  .signup-pill { left: 182px; top: 95px; width: 350px; height: 73px; }
  .signup-pill__text { position: absolute; left: 38px; top: 6px; color: var(--white); font-family: "Montserrat", sans-serif; font-weight: 700; font-size: 16.5px; line-height: 21px; }
  .band { left: 0; top: 172px; width: 891px; height: 364px; background: linear-gradient(180deg, var(--green) 0%, #2fb05e 55%, var(--teal) 100%); }
  .tab-why { left: 0; top: 176px; width: 150px; height: 33px; background: var(--navy); clip-path: polygon(0 0, 100% 0, 84% 100%, 0 100%); color: var(--white); font-family: "Montserrat", sans-serif; font-weight: 800; font-size: 19px; padding: 4px 0 0 18px; }
  .why-list { left: 18px; top: 215px; list-style: none; color: var(--white); font-size: 13.5px; line-height: 20.6px; }
  .why-list li { display: flex; align-items: center; gap: 6px; }
  .tick { width: 12px; height: 12px; flex: none; }
  .services-title { left: 0; top: 352px; width: 472px; height: 32px; background: var(--white); clip-path: polygon(0 0, 100% 0, 94% 100%, 0 100%); color: var(--navy); font-family: "Montserrat", sans-serif; font-weight: 700; font-size: 19px; padding: 3px 0 0 18px; }
  .services { top: 398px; list-style: none; color: var(--white); font-size: 14.5px; font-weight: 700; line-height: 26px; }
  .services li { display: flex; align-items: center; gap: 9px; }
  .services--left { left: 18px; }
  .services--right { left: 221px; }
  .svc-dot { width: 17px; height: 17px; border-radius: 50%; background: var(--white); flex: none; position: relative; }
  .svc-dot::after { content: ""; position: absolute; left: 5px; top: 5px; width: 7px; height: 7px; border-radius: 50%; background: var(--navy); }
  .footer-strip { left: 0; top: 540px; width: 891px; height: 78px; background: var(--navy); }
  .footer-contact { left: 0; top: 540px; width: 335px; height: 78px; background: var(--green); clip-path: polygon(0 0, 316px 0, 335px 39px, 316px 78px, 0 78px); }
  .contact { color: var(--white); font-family: "Oswald", sans-serif; font-weight: 500; font-size: 19px; line-height: 26px; }
  .contact--front { left: 18px; top: 551px; }
  .contact b { font-weight: 600; }
  .contact svg { width: 12px; height: 12px; vertical-align: 0; }
  .offer { left: 345px; top: 547px; color: var(--white); font-family: "Montserrat", sans-serif; }
  .offer__lead { font-weight: 700; font-size: 15px; }
  .offer__big { font-weight: 900; font-size: 37px; letter-spacing: 2px; line-height: 40px; }
  .offer-divider { left: 563px; top: 546px; height: 66px; border-left: 2px dotted var(--white); }
  .offer__tail { left: 577px; top: 551px; color: var(--white); font-family: "Montserrat", sans-serif; font-weight: 800; font-size: 20px; line-height: 26px; text-align: center; }
  .hex { left: 470px; top: 10px; width: 421px; height: 520px; }
  .phone-photo { left: 700px; top: 322px; width: 191px; height: 296px; border-radius: 26px 26px 0 60px; background: linear-gradient(160deg, #1d1d1f 0%, #2b8e4a 35%, #2fa35a 70%, #e9b89c 100%); }

  /* Back */
  .save { left: 24px; top: 26px; color: var(--green); font-family: "Oswald", sans-serif; font-weight: 600; line-height: 1; }
  .save__a { font-size: 34px; letter-spacing: .5px; }
  .save__a span { font-size: 44px; }
  .save__b { font-size: 66px; font-weight: 700; margin-top: 4px; }
  .save__c { font-size: 29px; margin-top: 10px; }
  .save__d { font-size: 37px; margin-top: 8px; font-weight: 700; }
  .houses { left: 30px; top: 240px; width: 450px; height: 80px; }
  .meter { left: 30px; top: 324px; width: 452px; height: 56px; border-radius: 28px; background: var(--grey-track); overflow: hidden; }
  .meter__fill { position: absolute; left: 0; top: 0; height: 100%; width: 370px; border-radius: 28px; background: linear-gradient(90deg, var(--navy) 0%, #2f6fc4 30%, var(--sky) 50%, #2bb36a 80%, var(--green) 100%); }
  .meter__label { position: absolute; top: 10px; font-family: "Montserrat", sans-serif; font-weight: 800; font-size: 27px; }
  .meter__label--five { left: 172px; color: var(--white); }
  .meter__label--ten { left: 377px; color: var(--navy); }
  .app-cta { left: 26px; top: 398px; font-family: "Montserrat", sans-serif; font-weight: 800; color: var(--navy); line-height: 1.15; }
  .app-cta__a { font-size: 27.5px; }
  .app-cta__b { font-size: 22px; }
  .app-cta__c { font-size: 43px; color: var(--sky); font-weight: 900; margin-top: 4px; }
  .back-band { left: 0; top: 536px; width: 460px; height: 82px; background: var(--navy); clip-path: polygon(0 0, 100% 0, 82% 100%, 0 100%); }
  .contact--back { left: 22px; top: 547px; }
  .indicia { left: 786px; top: 375px; width: 74px; height: 74px; border: 1px solid #555; font-family: "Arimo", Arial, sans-serif; font-size: 10px; line-height: 12px; text-align: center; color: var(--ink); padding-top: 7px; }
  .address { left: 585px; top: 488px; width: 247px; height: 99px; border: 1px solid #555; font-family: "Arimo", Arial, sans-serif; font-size: 14px; color: var(--ink); }
  .address__line { position: absolute; left: 74px; top: 12px; font-size: 11px; }
  .address__to { position: absolute; left: 18px; top: 48px; line-height: 16px; }
</style>
</head>
<body>
<div class="sheet">

  <!-- FRONT -->
  <section class="card card--front" aria-label="Postcard front">
    <div class="abs band"></div>

    <svg class="abs hex" viewBox="470 10 421 520" aria-hidden="false">
      <polygon points="667,30 868,138 868,398 667,506 490,398 490,138" fill="none" stroke="var(--navy)" stroke-width="34" stroke-linejoin="round"/>
      <polygon points="667,30 868,138 868,398 667,506 490,398 490,138" fill="var(--white)" stroke="var(--white)" stroke-width="12" stroke-linejoin="round"/>
      <polygon points="667,46 854,146 854,390 667,490 504,390 504,146" fill="url(#housePhoto)" stroke-linejoin="round" role="img" aria-label="Photo of a two-storey house with a trimmed green lawn under blue sky"/>
      <defs>
        <linearGradient id="housePhoto" x1="0" y1="0" x2="0" y2="1">
          <stop offset="0" stop-color="#5bb8ef"/>
          <stop offset=".45" stop-color="#9cc9e6"/>
          <stop offset=".62" stop-color="#6f8796"/>
          <stop offset=".8" stop-color="#5aa63a"/>
          <stop offset="1" stop-color="#3f8a2c"/>
        </linearGradient>
      </defs>
    </svg>

    <div class="abs brand">
      <span class="brand__dot"></span>
      <span class="brand__name">FERNQUILL</span>
    </div>

    <div class="abs headline">
      <div class="headline__top">LANDSCAPING SERVICE</div>
      <div class="headline__sub">RIGHT AT YOUR FINGERTIPS</div>
    </div>

    <div class="abs signup-pill">
      <svg width="350" height="73" viewBox="0 0 350 73">
        <path d="M36,0 H350 L318,73 H36 A36.5,36.5 0 0 1 36,0 Z" fill="var(--sky)"/>
        <g fill="none" stroke="var(--white)" stroke-width="2" stroke-linecap="round">
          <path d="M12,40 a10,10 0 0 1 20,0"/>
          <path d="M8,40 a14,14 0 0 1 28,0"/>
          <path d="M22,40 v14"/>
        </g>
      </svg>
      <div class="signup-pill__text">Sign Up With a Few Easy Steps<br>And Manage Your Account<br>From Our App or Online</div>
    </div>

    <div class="abs tab-why">WHY US</div>

    <ul class="abs why-list">
      <li><svg class="tick" viewBox="0 0 12 12"><rect x=".75" y=".75" width="10.5" height="10.5" fill="none" stroke="#fff" stroke-width="1.3"/><path d="M3 6l2 2 4-5" fill="none" stroke="#fff" stroke-width="1.5"/></svg>We are licensed and insured landscaping pros</li>
      <li><svg class="tick" viewBox="0 0 12 12"><rect x=".75" y=".75" width="10.5" height="10.5" fill="none" stroke="#fff" stroke-width="1.3"/><path d="M3 6l2 2 4-5" fill="none" stroke="#fff" stroke-width="1.5"/></svg>Real, instant, upfront pricing for mowing, mulching and most other services</li>
      <li><svg class="tick" viewBox="0 0 12 12"><rect x=".75" y=".75" width="10.5" height="10.5" fill="none" stroke="#fff" stroke-width="1.3"/><path d="M3 6l2 2 4-5" fill="none" stroke="#fff" stroke-width="1.5"/></svg>Automated safe &amp; secure transactions upon service completion and satisfaction</li>
      <li><svg class="tick" viewBox="0 0 12 12"><rect x=".75" y=".75" width="10.5" height="10.5" fill="none" stroke="#fff" stroke-width="1.3"/><path d="M3 6l2 2 4-5" fill="none" stroke="#fff" stroke-width="1.5"/></svg>Excellent customer service with our quality guaranteed commitment!</li>
      <li><svg class="tick" viewBox="0 0 12 12"><rect x=".75" y=".75" width="10.5" height="10.5" fill="none" stroke="#fff" stroke-width="1.3"/><path d="M3 6l2 2 4-5" fill="none" stroke="#fff" stroke-width="1.5"/></svg>Veteran owned</li>
      <li><svg class="tick" viewBox="0 0 12 12"><rect x=".75" y=".75" width="10.5" height="10.5" fill="none" stroke="#fff" stroke-width="1.3"/><path d="M3 6l2 2 4-5" fill="none" stroke="#fff" stroke-width="1.5"/></svg>A portion of our proceeds go to "Rennick Dolby Foundation"</li>
    </ul>

    <div class="abs services-title">List's out all of the services we will offer</div>

    <ul class="abs services services--left">
      <li><span class="svc-dot"></span>Mowing</li>
      <li><span class="svc-dot"></span>Mulching</li>
      <li><span class="svc-dot"></span>Aeration and Over-seeding</li>
      <li><span class="svc-dot"></span>Fertilization</li>
      <li><span class="svc-dot"></span>Shrub/Tree Trimming</li>
    </ul>
    <ul class="abs services services--right">
      <li><span class="svc-dot"></span>Leaf removal and yard clean up</li>
      <li><span class="svc-dot"></span>Accent lighting installation</li>
      <li><span class="svc-dot"></span>Sprinkler blow-out / Winterization</li>
      <li><span class="svc-dot"></span>Driveway pressure washing and sealing</li>
      <li><span class="svc-dot"></span>Firewood Delivery</li>
    </ul>

    <div class="abs footer-strip"></div>
    <div class="abs footer-contact"></div>
    <div class="abs contact contact--front">
      <div><b>CALL US</b> <svg viewBox="0 0 12 12"><path d="M2.5 1l2 2-1 1.5a7 7 0 0 0 4 4L9 7.5l2 2L9.5 11A9 9 0 0 1 1 2.5z" fill="#fff"/></svg> 999-4242-717</div>
      <div><b>VISIT US</b> <svg viewBox="0 0 12 12"><circle cx="6" cy="6" r="5" fill="none" stroke="#fff" stroke-width="1.2"/><path d="M1 6h10M6 1c-2.5 3-2.5 7 0 10M6 1c2.5 3 2.5 7 0 10" fill="none" stroke="#fff" stroke-width="1"/></svg> www.Fernquill.com</div>
    </div>
    <div class="abs offer">
      <div class="offer__lead">Sign up now and receive</div>
      <div class="offer__big">50% OFF</div>
    </div>
    <div class="abs offer-divider"></div>
    <div class="abs offer__tail">Your First<br>Mow!</div>

    <div class="abs phone-photo" role="img" aria-label="Hand holding a smartphone showing the Fernquill instant quote screen"></div>
  </section>

  <!-- BACK -->
  <section class="card card--back" aria-label="Postcard back">
    <svg class="abs" style="left:0;top:0" width="891" height="618" viewBox="0 0 891 618" aria-hidden="true">
      <path d="M335,-5 L505,95 Q530,110 530,140 L530,440 Q530,470 505,490 L440,540" fill="none" stroke="var(--navy)" stroke-width="11" stroke-linejoin="round"/>
    </svg>

    <div class="abs save">
      <div class="save__a"><span>Y</span>OU COULD SAVE UP TO</div>
      <div class="save__b">10% OFF OUR</div>
      <div class="save__c">ALREADY LOW PRICES, AS MORE OF</div>
      <div class="save__d">YOUR NEIGHBORS SIGN UP!</div>
    </div>

    <svg class="abs houses" viewBox="0 0 450 80" aria-hidden="true">
      <path d="M26,44 L45,62 H39 V80 H13 V62 H7 Z" fill="var(--navy)"/>
      <path d="M193,28 L221,54 H213 V80 H173 V54 H165 Z" fill="var(--sky)"/>
      <path d="M355,2 L395,40 H384 V80 H326 V40 H315 Z" fill="var(--green)"/>
      <rect x="345" y="55" width="20" height="25" fill="var(--white)"/>
      <rect x="188" y="64" width="11" height="16" fill="var(--white)"/>
      <rect x="22" y="70" width="8" height="10" fill="var(--white)"/>
    </svg>

    <div class="abs meter" role="img" aria-label="Neighborhood savings meter from 5% to 10%">
      <div class="meter__fill"></div>
      <span class="meter__label meter__label--five">5%</span>
      <span class="meter__label meter__label--ten">10%</span>
    </div>

    <div class="abs app-cta">
      <div class="app-cta__a">CHECK OUT OUR APP TODAY</div>
      <div class="app-cta__b">TO SEE HOW MUCH NEIGHBORS ARE</div>
      <div class="app-cta__c">ALREADY SAVING!</div>
    </div>

    <div class="abs back-band"></div>
    <div class="abs contact contact--back">
      <div><b>CALL US</b> <svg viewBox="0 0 12 12"><path d="M2.5 1l2 2-1 1.5a7 7 0 0 0 4 4L9 7.5l2 2L9.5 11A9 9 0 0 1 1 2.5z" fill="#fff"/></svg> 999-4242-717</div>
      <div><b>VISIT US</b> <svg viewBox="0 0 12 12"><circle cx="6" cy="6" r="5" fill="none" stroke="#fff" stroke-width="1.2"/><path d="M1 6h10M6 1c-2.5 3-2.5 7 0 10M6 1c2.5 3 2.5 7 0 10" fill="none" stroke="#fff" stroke-width="1"/></svg> www.Fernquill.com</div>
    </div>

    <div class="abs indicia">PRSRT STD<br>ECRWSS<br>U.S. Postage<br><b>PAID</b><br>ORTQ RETAIL</div>

    <div class="abs address">
      <div class="address__line">****************ECRWSS****</div>
      <div class="address__to">Local<br>Postal Customer</div>
    </div>
  </section>

</div>
</body>
</html>
```